Skin Brightening Poster Design Project

Poster design to promote skin brightening treatments during winter months.

Requirements
Must have
• Poster must be eye catching to both males and females.

List of services: IPL, Laser, Microdermabrasion, Peels

Dr. Welsford's Radiance Cream now available

Free consultations

Clinic details:
CBD: Suite 304, 7 Farrow Street Melbourne 9718 2043
Richmond: 415 Garnet Street Richmond 9386 5172
Dandenong: Shop 9 The Lantern Mall, Dandenong 9541 7630

Web site: www.dermalivo.com.au

A1 size poster
Should not have
• Poster design should not be similar to day spas, hairdressers or beauty salons

```html
<!DOCTYPE html>
<html lang="en">
<head>
<meta charset="utf-8">
<title>Skin Brightening Poster</title>
<link href="https://fonts.googleapis.com/css2?family=Arimo:wght@400;700&display=swap" rel="stylesheet">
<style>
  :root {
    --paper: #ffffff;
    --plum: #8a3f8f;
    --ink: #3a3a3a;
    --grey: #555555;
    --skin-light: #f1e6e0;
    --skin-mid: #e4d3cb;
    --skin-shadow: #cdb8ae;
  }
  html, body {
    margin: 0;
    padding: 0;
    overflow: hidden;
    background: var(--paper);
  }
  .poster {
    position: relative;
    width: 849px;
    height: 1200px;
    overflow: hidden;
    background: var(--paper);
    font-family: "Arimo", Arial, sans-serif;
  }
  .portrait {
    position: absolute;
    left: 0;
    top: 0;
    width: 600px;
    height: 1200px;
    background:
      radial-gradient(ellipse 60% 45% at 30% 40%, var(--skin-mid) 0%, rgba(228,211,203,0) 70%),
      linear-gradient(90deg, var(--skin-shadow) 0%, var(--skin-light) 55%, rgba(255,255,255,0) 100%);
  }
  .brand {
    position: absolute;
    right: 96px;
    top: 78px;
    display: flex;
    align-items: center;
    gap: 10px;
    color: var(--plum);
    font-weight: 400;
    font-size: 22px;
    letter-spacing: 0.5px;
  }
  .brand-mark {
    width: 14px;
    height: 14px;
    background: var(--plum);
  }
  .services {
    position: absolute;
    right: 78px;
    top: 350px;
    margin: 0;
    padding: 0;
    list-style: none;
    text-align: right;
    color: var(--ink);
    font-weight: 700;
    font-size: 34px;
    line-height: 46px;
  }
  .product {
    position: absolute;
    right: 78px;
    top: 650px;
    margin: 0;
    text-align: right;
    color: var(--plum);
    font-weight: 700;
    font-size: 24px;
    line-height: 31px;
  }
  .offer {
    position: absolute;
    right: 78px;
    top: 748px;
    margin: 0;
    color: var(--plum);
    font-weight: 700;
    font-size: 35px;
  }
  .clinics {
    position: absolute;
    right: 78px;
    top: 982px;
    margin: 0;
    text-align: right;
    color: var(--grey);
    font-weight: 700;
    font-size: 14.5px;
    line-height: 22px;
    font-style: normal;
  }
  .website {
    position: absolute;
    right: 78px;
    top: 1122px;
    margin: 0;
    color: var(--plum);
    font-weight: 700;
    font-size: 19px;
  }
</style>
</head>
<body>
  <main class="poster">
    <div class="portrait" role="img" aria-label="Close-up portrait of a woman's face with clear, bright skin, fading into white"></div>

    <div class="brand">
      <span class="brand-mark"></span>
      <span class="brand-name">Yarra Dermal Institute</span>
    </div>

    <ul class="services">
      <li>IPL</li>
      <li>Laser</li>
      <li>Microdermabrasion</li>
      <li>Peels</li>
    </ul>

    <p class="product">Dr. Welsford's Radiance Cream<br>now available!</p>

    <p class="offer">FREE CONSULTATIONS</p>

    <address class="clinics">
      CBD: Suite 304, 7 Farrow Street Melbourne 9718 2043<br>
      Richmond: 415 Garnet Street Richmond 9386 5172<br>
      Dandenong: Shop 9 The Lantern Mall, Dandenong 9541 7630
    </address>

    <p class="website">www.dermalivo.com.au</p>
  </main>
</body>
</html>
```